Redesign Opal's RV Park & Lodge Website, Brenna, North Dakota

I need a totally re-designed website for my RV Park / Lodge. I want to not only provide information on my RV Park / Lodge, I want to provide my customers with information on the town and area attractions. I want to provide rate information. Ideally, I would like to have a button/page for each section: Welcome & Information, Area Attractions, Welcome to Brenna, Rates, Who's Opal?!, FAQ's and Where are we?. I don't know if this would be more expensive the more pages you have? If more pages is too expensive, then we can combine info on less pages. I want my logo included on the web page. I want Mockup Forge to take down my old website and use the same address to put up my newly designed website.

Target Market(s)

Full time RVers, People who camp, hunt fish, People who recreate on Heron Lake, People who are looking for meeting/conference space, people who are looking for party venue

Industry/Entity Type

Accommodation

Number of Pages Required

3 page

Requirements
Must have
• I want a cozy, welcoming type web site. No super dark colors. Bright and cheerful.
• Must be simple and organized.
• NOTE: I have a file of pictures of the interior of Opal's Lodge that must be included in website. Please request this file if you will be designing my project as the files are too large to upload through Mockup Forge.
Nice to have
• If you cannot open any of the files listed, please notify me.
Should not have
• No stark or super-formal designs.

```html
<!DOCTYPE html>
<html lang="en">
<head>
<meta charset="utf-8">
<title>Opal's RV Park &amp; Lodge – Brenna, North Dakota</title>
<link rel="stylesheet" href="https://fonts.googleapis.com/css2?family=Montserrat:wght@400;500;600;700&family=Open+Sans:wght@400;600&display=swap">
<style>
:root{
  --green:#3c5a1d;
  --maroon:#6a1820;
  --ink:#333;
  --muted:#666;
  --pale:#f1f1f4;
  --white:#fff;
  --footer-black:#1d1d1d;
}
*{margin:0;padding:0;box-sizing:border-box}
html,body{width:1200px;height:3416px;overflow:hidden}
body{position:relative;background:var(--white);font-family:"Open Sans",Arial,sans-serif;color:var(--ink)}
.abs{position:absolute}
h1,h2,h3,h4{font-family:"Montserrat",Arial,sans-serif;font-weight:500}

/* header */
.topbar{left:0;top:0;width:1200px;height:100px;background:var(--white)}
.call{right:88px;top:22px;display:flex;align-items:center;gap:14px;font-family:"Montserrat",sans-serif;font-size:17px;color:var(--maroon)}
.call-icon{width:56px;height:56px;border-radius:50%;background:var(--maroon);display:flex;align-items:center;justify-content:center}
.nav{left:0;top:100px;width:1200px;height:60px;background:var(--green)}
.nav ul{list-style:none;position:absolute;left:303px;top:0;width:810px;height:60px;display:flex;align-items:center;justify-content:space-between}
.nav li{font-family:"Montserrat",sans-serif;font-size:10.5px;font-weight:600;color:var(--white);letter-spacing:.2px;white-space:nowrap}
.brand-badge{left:86px;top:6px;width:192px;height:192px;border-radius:50%;background:var(--white);display:flex;align-items:flex-end;justify-content:center;text-align:center;padding-bottom:34px;z-index:3}
.brand-name{font-family:"Montserrat",sans-serif;font-weight:600;font-size:18px;line-height:1.2;color:var(--maroon);width:160px}

/* hero */
.hero{left:0;top:160px;width:1200px;height:482px;background:linear-gradient(180deg,#c9cfd4 0%,#b2b6b5 38%,#8c8e80 62%,#6f8a4c 80%,#5f7d3a 100%)}
.hero-card{left:114px;top:382px;width:428px;height:164px;background:rgba(60,90,29,.82);padding:22px 26px 0 28px;color:var(--white)}
.hero-card h1{font-size:33px;font-weight:500;margin-bottom:12px;white-space:nowrap}
.hero-card p{font-size:11.5px;line-height:1.85}
.dots{left:566px;top:611px;display:flex;gap:8px}
.dots span{width:16px;height:16px;border:2px solid var(--white);border-radius:50%}
.dots span.on{background:var(--white)}

/* welcome */
.welcome{left:0;top:684px;width:1200px;text-align:center}
.welcome h2{font-size:26px;color:#222;letter-spacing:.5px}
.welcome h3{font-size:18px;font-weight:600;color:var(--green);margin-top:8px;letter-spacing:.4px}
.welcome p{font-size:11.5px;line-height:2.2;color:var(--muted);width:700px;margin:20px auto 0}
.rule{left:86px;top:854px;width:1028px;height:1px;background:#e2e2e2}

.section-title{font-size:20px;font-weight:600;color:var(--green);letter-spacing:.4px}
.body-copy{font-size:11.5px;line-height:2.3;color:var(--muted)}
.photo{border-radius:50%;border:4px solid var(--white);box-shadow:0 0 0 1px #d7d7d7}

.lodge-intro{left:86px;top:912px;width:530px}
.lodge-intro p{margin-top:26px}

.meeting-band{left:0;top:1229px;width:1200px;height:376px;background:var(--pale)}
.meeting-copy{left:537px;top:1328px;width:480px}
.meeting-copy p{margin-top:24px}

/* split */
.split{left:0;top:1605px;width:1200px;height:508px}
.split svg{position:absolute;left:0;top:0}
.split-col{color:var(--white)}
.split-col h2{font-size:25px;font-weight:500;color:var(--white);letter-spacing:.3px}
.ticks{list-style:none}
.ticks li{position:relative;padding-left:34px;font-size:11.5px;line-height:1.45}
.ticks li::before{content:"";position:absolute;left:6px;top:2px;width:5px;height:10px;border-right:2px solid var(--white);border-bottom:2px solid var(--white);transform:rotate(45deg)}
.lodge-list{left:86px;top:1645px;width:520px}
.lodge-list .ticks{margin-top:30px}
.lodge-list .ticks li{margin-bottom:13.2px}
.park-list{left:653px;top:1645px;width:470px}
.park-list p{font-size:11.5px;line-height:2;margin-top:16px}
.park-list .ticks{margin-top:12px}
.park-list .ticks li{margin-bottom:10.6px}

/* tents */
.tents{left:103px;top:2232px}
.tents h2{font-size:46px;font-weight:600;color:var(--green);letter-spacing:1px}
.tents h3{font-size:25px;font-weight:500;color:#6b6b6b;letter-spacing:.8px;margin-top:6px}

/* social band */
.social-band{left:0;top:2482px;width:1200px;height:109px;background:var(--green)}
.social-band p{position:absolute;left:129px;top:30px;font-family:"Montserrat",sans-serif;font-size:13.5px;font-weight:600;color:var(--white);line-height:2.05;letter-spacing:.3px}
.social-btn{position:absolute;left:826px;top:27px;width:233px;height:57px;background:var(--maroon);display:flex;align-items:center;justify-content:center;gap:12px;font-family:"Montserrat",sans-serif;font-weight:600;font-size:24px;color:var(--white)}
.social-btn i{width:14px;height:14px;background:var(--white);display:block}

/* rates */
.rates-title{left:0;top:2615px;width:1200px;text-align:center;font-size:27px;font-weight:600;color:var(--green);letter-spacing:.6px}
.rate-card{background:var(--white);box-shadow:0 0 0 1px #e4e4e4,0 2px 6px rgba(0,0,0,.06)}
.rate-card header{height:46px;display:flex;align-items:center;justify-content:center;font-family:"Montserrat",sans-serif;font-weight:600;font-size:15px;color:var(--white);letter-spacing:.3px}
.rate-card .inner{padding:24px 20px 0}
.rate-card h4{font-size:14px;font-weight:600;color:var(--green);margin-bottom:18px}
.rate-card p{font-size:11.3px;line-height:2.1;color:var(--muted);margin-bottom:18px}
.head-maroon{background:var(--maroon)}
.head-green{background:var(--green)}

/* footer */
.footer{left:0;top:3069px;width:1200px;height:283px;background:var(--pale)}
.footer-brand{left:135px;top:3092px;width:230px;text-align:center}
.footer-brand .brand-name{font-size:26px;width:auto;line-height:1.25;color:var(--maroon)}
.footer-brand .mark{width:38px;height:38px;background:var(--green);margin:0 auto 14px}
.footer-col h4{font-size:15px;font-weight:600;color:#444;letter-spacing:.4px}
.contact{left:394px;top:3134px;width:230px}
.contact ul{list-style:none;margin-top:24px}
.contact li{display:flex;align-items:center;gap:14px;font-size:11.5px;color:#555;margin-bottom:13px;white-space:nowrap}
.contact svg{flex:none}
.newsletter{left:640px;top:3134px;width:215px}
.newsletter p{font-size:11.5px;color:#555;line-height:1.75;margin-top:22px}
.news-input{margin-top:14px;width:215px;height:34px;border:1px solid #d0d0d0;background:var(--white);font-size:11px;color:#666;padding:10px 10px}
.news-btn{margin-top:12px;display:inline-block;background:var(--green);color:var(--white);font-size:11px;font-weight:600;padding:7px 9px}
.map{left:879px;top:3126px;width:230px;height:169px;border:1px solid #bbb;background:linear-gradient(135deg,#f4f3ee,#e6e8dc 60%,#d9dfc6)}
.bottombar{left:0;top:3352px;width:1200px;height:64px;background:var(--footer-black)}
.bottombar p{position:absolute;left:86px;top:24px;font-size:11.5px;color:#ddd}
.circles{position:absolute;left:906px;top:15px;display:flex;gap:9px}
.circles span{width:35px;height:35px;border-radius:50%;border:2px solid #ddd}
</style>
</head>
<body>

<div class="abs topbar"></div>
<div class="abs brand-badge"><div class="brand-name">Opal's RV Park &amp; Lodge Brenna ND</div></div>
<div class="abs call">
  <span class="call-icon"><svg width="20" height="20" viewBox="0 0 24 24"><path fill="#fff" d="M6.6 10.8a15.1 15.1 0 0 0 6.6 6.6l2.2-2.2c.3-.3.7-.4 1-.2 1.1.4 2.3.6 3.6.6.6 0 1 .4 1 1V20c0 .6-.4 1-1 1A17 17 0 0 1 3 4c0-.6.4-1 1-1h3.5c.6 0 1 .4 1 1 0 1.3.2 2.5.6 3.6.1.3 0 .7-.2 1z"/></svg></span>
  <span>Call Us : 701-555-0148</span>
</div>
<nav class="abs nav">
  <ul>
    <li>HOME</li><li>WELCOME &amp; INFORMATION</li><li>AREA ATTRACTIONS</li><li>WELCOME TO BRENNA</li><li>RATES</li><li>WHO'S OPAL?!</li><li>FAQ'S &amp; WHERE ARE WE</li>
  </ul>
</nav>

<div class="abs hero" role="img" aria-label="Photo of the red and grey steel lodge building on green prairie grass"></div>
<div class="abs hero-card">
  <h1>Opal RV Park &amp; Logde</h1>
  <p>Sed ut perspiciatis unde omnis iste natus error sit voluptatem accu-santium doloremque laudantium, totam rem aperiam, eaque ipsa quae quasi architecto beatae vitae dicta sunt explicabo.</p>
</div>
<div class="abs dots"><span class="on"></span><span></span><span></span></div>

<section class="abs welcome">
  <h2>WELCOME TO</h2>
  <h3>OPAL'S RV PARK &amp; LODGE &amp; BRENNA, NORTH DAKOTA</h3>
  <p>Brenna is in the heart of some of the greatest hunting and fishing in the world. Opal's RV Park is located right on Highway 9 midway between Heron Lake and Pine Ridge North Dakota. We are smack dab in the middle of it all!</p>
</section>
<div class="abs rule"></div>

<section class="abs lodge-intro">
  <h2 class="section-title">OPAL'S LODGE</h2>
  <p class="body-copy">Are you looking for a cozy, but spacious home away from home? Well, you have found it! Opal's Lodge is 2200 square feet of living space. There are 2 spacious bedrooms with queen sized beds and another common sleeping area with 5 sets of bunk beds. Available to you are 2 restrooms with showers, a great room with dining and relaxing space and a full kitchen. Everything is supplied for you: towels, bedding, cookware, dishware, grill and etc...all that you need to make your stay worry and hassle free. Throw some clothes in a suitcase, hit the road and we will have your home away from home all ready when you get here! The Lodge is open all year round.</p>
</section>
<div class="abs photo" style="left:729px;top:888px;width:300px;height:300px;background:radial-gradient(circle at 50% 40%,#d9c7b4,#9a9488 70%,#6e6b62)" role="img" aria-label="Portrait photo of the lodge owner"></div>

<div class="abs meeting-band"></div>
<div class="abs photo" style="left:182px;top:1266px;width:300px;height:300px;background:radial-gradient(circle at 50% 55%,#c9b7a3,#8f6f5e 60%,#5c4a3f)" role="img" aria-label="Photo of the lodge great room set with tables for a meeting"></div>
<section class="abs meeting-copy">
  <h2 class="section-title">MEETING / CONFERENCE SPACE</h2>
  <p class="body-copy">Are you looking for a venue for your next meeting, training event, guys/girls weekend, quilt retreat, holiday gathering, family reunion, birthday, wedding party or get-together? We've got you covered! Opal's Lodge seats about 65 people comfortably. Many of our customers have commented that Opal's was the perfect place for their event because it was so inviting...and just like home!</p>
</section>

<section class="abs split">
  <svg width="1200" height="508" viewBox="0 0 1200 508">
    <polygon points="0,0 644,0 553,508 0,508" fill="#3c5a1d"/>
    <polygon points="644,0 1200,0 1200,508 553,508" fill="#6a1820"/>
  </svg>
</section>
<div class="abs split-col lodge-list">
  <h2>OPAL'S LODGE</h2>
  <ul class="ticks">
    <li>Groups – hunting, fishing, working, playing</li>
    <li>2200 square feet</li>
    <li>Full kitchen</li>
    <li>Free WiFi</li>
    <li>Satellite TV</li>
    <li>2 restrooms, one is handicap accessible</li>
    <li>Sleeps 14 – 2 bedrooms with queen sized beds, plus a shared sleeping area with bunk</li>
    <li>A great room with ample seating for large groups</li>
    <li>Opal's supplies everything...bedding, towels, cookware, etc.</li>
    <li>Kids stay free</li>
  </ul>
</div>
<div class="abs split-col park-list">
  <h2>Opal's RV PARK</h2>
  <p>Opal's RV Park sits right next to Highway 9 on the north side. We have 14 full service spaces – sewer, water and electric (20, 30, 50 amp). There is an indoor restroom with shower that is available 24 hours a day to our RV customers. Plenty of space is available to you for parking boats, trailers, etc.Opal's RV Park year round, but water usage depends on when spring thaw and freeze up occurs.Please note: Opal's RV Park is an unattended RV park.</p>
  <ul class="ticks">
    <li>14 Full Service Sites</li>
    <li>Free WiFi</li>
    <li>Safe &amp; convenient location</li>
    <li>24 hour indoor restroom with shower</li>
    <li>Roadpass Club accepted for first night</li>
    <li>Ample room to park boats, trailers etc.</li>
    <li>Convenience store/gas station located right across the street. Restaurant onsite.</li>
    <li>Opal's operates on a first come, first serve basis for short term stays. If you would like to reserve for a stay longer than 3 days, please call Opal.</li>
  </ul>
</div>

<section class="abs tents">
  <h2>TENTS</h2>
  <h3>PRIMITIVE &amp; TENT SITES ARE ALSO AVAILABLE</h3>
</section>
<div class="abs photo" style="left:737px;top:2149px;width:292px;height:292px;background:radial-gradient(circle at 50% 60%,#3d4f8c,#6f86b8 55%,#a9c0de)" role="img" aria-label="Photo of a blue farm tractor under a clear sky"></div>

<section class="abs social-band">
  <p>FIND OUT WHAT OUR CUSTOMERS ARE SAYING ABOUT OPAL'S RV PARK &amp; LODGE.<br>CHECK OUT OUR TRAILBOOK PAGE</p>
  <div class="social-btn"><i></i>trailbook</div>
</section>

<h2 class="abs rates-title">RATES</h2>
<article class="abs rate-card" style="left:100px;top:2673px;width:310px;height:242px">
  <header class="head-maroon">OPAL'S LODGE PRICING</header>
  <div class="inner">
    <h4>$200 FOR 24 HOURS</h4>
    <p>The first 6 adults are included in the $200 per night rent. Each adult exceeding the initial 6, must pay $25 per night. Kids under age 16 stay free.</p>
  </div>
</article>
<article class="abs rate-card" style="left:442px;top:2673px;width:309px;height:355px">
  <header class="head-green">OPAL'S RV PARK PRICING</header>
  <div class="inner">
    <h4>$24/NIGHT $125/WEEK $375/MONTH</h4>
    <p>This price is for 4 adults. Any adults exceeding the initial 4, must pay $5 extra per night. Kids under 16 stay free.</p>
    <h4>$12/NIGHT</h4>
    <p>This price is for 4 adults. Any adults exceeding the initial 4, must pay $3 extra per night. Kids under 16 stay free</p>
  </div>
</article>
<article class="abs rate-card" style="left:786px;top:2673px;width:310px;height:242px">
  <header class="head-maroon">SHOWERS</header>
  <div class="inner">
    <h4>$200 FOR 24 HOURS</h4>
    <p>Showers are $5 per person for unregistered customers. There is no charge for anyone that uses the shower that is staying at Opal's RV Park &amp; Lodge</p>
  </div>
</article>

<footer class="abs footer"></footer>
<div class="abs footer-brand">
  <div class="mark"></div>
  <div class="brand-name">Opal's RV Park<br>&amp; Lodge<br>Brenna ND</div>
</div>
<div class="abs contact footer-col">
  <h4>CONTACT US</h4>
  <ul>
    <li><svg width="14" height="14" viewBox="0 0 24 24"><path fill="#666" d="M6.6 10.8a15.1 15.1 0 0 0 6.6 6.6l2.2-2.2c.3-.3.7-.4 1-.2 1.1.4 2.3.6 3.6.6.6 0 1 .4 1 1V20c0 .6-.4 1-1 1A17 17 0 0 1 3 4c0-.6.4-1 1-1h3.5c.6 0 1 .4 1 1 0 1.3.2 2.5.6 3.6.1.3 0 .7-.2 1z"/></svg>701-555-0148 (Phone)</li>
    <li><svg width="14" height="14" viewBox="0 0 24 24"><rect x="4" y="9" width="16" height="10" fill="#666"/><rect x="7" y="3" width="10" height="6" fill="none" stroke="#666" stroke-width="2"/></svg>701-555-0173 (Fax)</li>
    <li><svg width="14" height="14" viewBox="0 0 24 24"><rect x="3" y="5" width="18" height="14" fill="none" stroke="#666" stroke-width="2"/><path d="M3 6l9 7 9-7" fill="none" stroke="#666" stroke-width="2"/></svg>opalsrvpark@mailbox.test</li>
    <li><svg width="14" height="14" viewBox="0 0 24 24"><path fill="#666" d="M12 2a7 7 0 0 0-7 7c0 5 7 13 7 13s7-8 7-13a7 7 0 0 0-7-7zm0 9.5a2.5 2.5 0 1 1 0-5 2.5 2.5 0 0 1 0 5z"/></svg>214 Prairie Ave SE Brenna ND 58999</li>
  </ul>
</div>
<div class="abs newsletter footer-col">
  <h4>NEWSLETTER</h4>
  <p>Register Your email address to get information about us</p>
  <div class="news-input">Email Address</div>
  <div class="news-btn">SUBSCRIBE</div>
</div>
<div class="abs map" role="img" aria-label="Regional road map with the park area highlighted"></div>

<div class="abs bottombar">
  <p>© Copyright 2018 &nbsp;Opal RV Park &amp; Logde All Rights Reserved</p>
  <div class="circles"><span></span><span></span><span></span><span></span><span></span></div>
</div>

</body>
</html>
```